Gather the Marrow Book Cover

Looking for a cover for my book, Gather the Marrow. Part memoir, part self help - this book is one woman's journey breaking free of the patriarchy and stepping into her divine purpose. Think "boss ass bitch" in NYC transitions to Spiritual Goddess to the beaches of Costa Rica. We are playing on the archetypes of Wounded Masculine to Divine Feminine. Breaking the mold of being a good girl and owning her wild.

Target Market(s)

25-35 yr old female

Industry/Entity Type

Personal Development, Memoir

Other font styles liked:
• Pink #ff0099 Yellow #ffdf2b Teal #1fc4cd Gather - Brittany The - open sans Marrow - Bebas Neue

Colors
FFF300
FFF600
FEFA6F
FFFEC7
FFFEE8
E54698
E96AAD
F1A4CE
F9D9EA
FCEFF6

Requirements
Nice to have

```html
<!DOCTYPE html>
<html lang="en">
<head>
<meta charset="utf-8">
<title>Gather the Marrow — Book Cover</title>
<link rel="stylesheet" href="https://fonts.googleapis.com/css2?family=Sacramento&family=Bebas+Neue&family=Open+Sans:ital,wght@1,400&display=swap">
<style>
  :root {
    --backdrop: #000000;
    --pink: #ea168f;
    --yellow: #f3ea2a;
    --title-yellow: #ede53a;
    --white: #ffffff;
    --subtitle-grey: #787462;
    --ink: #0b0b0c;
  }
  * { margin: 0; padding: 0; box-sizing: border-box; }
  html, body {
    width: 927px;
    height: 1200px;
    overflow: hidden;
    background: var(--backdrop);
  }
  .cover {
    position: absolute;
    left: 136px;
    top: 109px;
    width: 655px;
    height: 981px;
    background: var(--yellow);
    overflow: hidden;
  }
  .title-band {
    position: absolute;
    left: 0;
    top: 0;
    width: 100%;
    height: 472px;
    background: var(--pink);
  }
  .title {
    font-weight: 400;
  }
  .title-script {
    position: absolute;
    left: 40px;
    top: 10px;
    width: 550px;
    text-align: center;
    font-family: "Sacramento", cursive;
    font-weight: 400;
    font-size: 230px;
    line-height: 1;
    color: var(--white);
  }
  .title-article {
    position: absolute;
    left: 394px;
    top: 222px;
    font-family: "Open Sans", sans-serif;
    font-style: italic;
    font-weight: 400;
    font-size: 34px;
    line-height: 1;
    color: var(--white);
  }
  .title-main {
    position: absolute;
    left: 0;
    top: 302px;
    width: 100%;
    text-align: center;
    font-family: "Bebas Neue", sans-serif;
    font-weight: 400;
    font-size: 180px;
    line-height: 1;
    letter-spacing: 2px;
    color: var(--title-yellow);
  }
  .portrait {
    position: absolute;
    left: 372px;
    top: 472px;
    width: 283px;
    height: 509px;
    z-index: 1;
  }
  .subtitle {
    position: absolute;
    left: 46px;
    top: 527px;
    z-index: 2;
    font-family: "Bebas Neue", sans-serif;
    font-weight: 400;
    font-size: 48px;
    line-height: 46px;
    color: var(--subtitle-grey);
    white-space: nowrap;
  }
</style>
</head>
<body>
  <main class="cover">
    <header class="title-band">
      <h1 class="title">
        <span class="title-script">Gather</span>
        <span class="title-article">the</span>
        <span class="title-main">MARROW</span>
      </h1>
    </header>
    <svg class="portrait" role="img" aria-label="Illustration: profile silhouette of a woman with upswept hair and a patterned round earring" viewBox="0 0 283 509">
      <defs>
        <linearGradient id="portrait-fill" x1="0" y1="0" x2="0" y2="1">
          <stop offset="0" stop-color="#1a1a17"/>
          <stop offset="1" stop-color="#0b0b0c"/>
        </linearGradient>
      </defs>
      <rect width="283" height="509" fill="url(#portrait-fill)"/>
    </svg>
    <p class="subtitle">Woman's journey<br>breaking free of<br>the patriarchy and<br>stepping into her<br>divine purpose</p>
  </main>
</body>
</html>
```